New York Property Management Company needs a Brochure Designed

We need a brochure for a new property management company in New York called KT7 Realty Partners. The 2 is superscript (squared.) We are looking for buildings to manage and want to showcase our expertise and caring. Logo is attached. We are getting a different photo and do not need all the verbiage. Also, does not need to be a trifold.
Updates

Property management group is a RESIDENTIAL property management group. I neglected to mention that. Thanks.

Hi designers, We've received very few designs so far so we've extended the deadline. We're hoping to receive your creative submissions soon! Thank you!

Reason: A few people have to weigh in on the design and it has been difficult coordinating this. We are getting close to making a decision and just need a few more days.

Industry/Entity Type

Property Management

```html
<!DOCTYPE html>
<html lang="en">
<head>
<meta charset="utf-8">
<title>KT7 Realty Partners Brochure</title>
<link rel="stylesheet" href="https://fonts.googleapis.com/css2?family=Open+Sans:wght@400;600;700&family=Arimo:wght@400;700&display=swap">
<style>
  :root {
    --purple: #662d8f;
    --purple-dark: #57267c;
    --orange: #f6a623;
    --white: #ffffff;
    --panel-grey: #d9d9db;
    --logo-grey: #5b6663;
    --text: #3a3a3a;
    --crop: #333333;
  }
  * { box-sizing: border-box; margin: 0; padding: 0; }
  html, body { width: 1200px; height: 881px; overflow: hidden; background: var(--white); }
  body { position: relative; font-family: "Arimo", Arial, sans-serif; color: var(--text); }

  .crop-marks { position: absolute; inset: 0; width: 1200px; height: 881px; pointer-events: none; }

  .cover-band {
    position: absolute; left: 34px; top: 22px; width: 1130px; height: 406px;
    background: linear-gradient(135deg, var(--purple) 0%, var(--purple-dark) 100%);
  }

  .brand-mark {
    position: absolute; left: 230px; top: 122px; width: 183px; height: 182px;
    background: var(--white); padding: 10px;
  }
  .brand-mark__square {
    width: 100%; height: 100%; background: var(--logo-grey);
    display: flex; align-items: center; justify-content: center; text-align: center;
    font-family: "Open Sans", Arial, sans-serif; font-weight: 600; color: var(--white);
    font-size: 19px; line-height: 1.25; letter-spacing: 1px;
  }

  .cover-contact {
    position: absolute; left: 120px; top: 362px; width: 410px; text-align: center;
    font-size: 11.5px; line-height: 15px; color: var(--white);
  }

  .cover-title { position: absolute; left: 668px; top: 150px; font-family: "Open Sans", Arial, sans-serif; }
  .cover-title__mark { font-size: 62px; font-weight: 700; color: var(--orange); line-height: 70px; }
  .cover-title__mark sup { font-size: 34px; vertical-align: 26px; }
  .cover-title__name { font-size: 21px; color: var(--white); line-height: 26px; margin-left: 2px; }
  .cover-title__suffix { font-size: 16px; color: var(--white); line-height: 20px; margin-left: 112px; }

  .founders-photo {
    position: absolute; left: 886px; top: 62px; width: 216px; height: 324px;
    background: linear-gradient(180deg, #b9c4cf 0%, #8f8a84 45%, #4a4d58 75%, #b7b0a6 100%);
  }

  .services-panel {
    position: absolute; left: 34px; top: 454px; width: 562px; height: 408px;
    background: var(--panel-grey); padding: 22px 12px 0 14px;
  }
  .services-panel p, .bios p {
    font-size: 8.3px; line-height: 10.6px; margin-bottom: 11px;
  }
  .services-panel .gap { margin-top: 33px; }
  .services-panel .point { margin-bottom: 13px; }

  .bios { position: absolute; left: 613px; top: 455px; width: 548px; }
  .bios h2 { font-size: 8.6px; font-weight: 700; margin-bottom: 11px; }
</style>
</head>
<body>

<div class="cover-band"></div>

<div class="brand-mark">
  <div class="brand-mark__square">KT7 REALTY<br>PARTNERS</div>
</div>

<div class="cover-contact">
  KT7 Realty Partners, LLC • 48 West 27th St., Ste. 410&nbsp; New York, NY&nbsp; 10001<br>
  212.555.0147<br>
  www.KT7RP.com
</div>

<div class="cover-title">
  <div class="cover-title__mark">KT7</div>
  <div class="cover-title__name">Realty Partners,</div>
  <div class="cover-title__suffix">LLC</div>
</div>

<div class="founders-photo" role="img" aria-label="Photo of the two founders standing on a Manhattan rooftop with apartment towers behind them"></div>

<section class="services-panel">
  <p>At KT7 Realty Partners, we manage each building as if it were our own; return each phone call; respond to each email; negotiate the best possible pricing on goods and services; address building needs in a respectful, practical, efficient and economic manner.</p>
  <p>We manage buildings with the highest level of service.&nbsp; Management is about service; it is knowing the operations of a building, but it is so much more.&nbsp; It is understanding resident and owner needs, identifying opportunities for creating value and providing a well-run and supportive community.</p>
  <p>Management encompasses all building services including, but not limited to, billing, collections, staff management, maintenance, compliance, capital projects and communication with owners, residents, vendors and building professionals.&nbsp; We do this by using established, reputable and reliable business partners.</p>
  <p>In order for our philosophy to succeed, a manager must be more than just an employee.&nbsp; KT7RP provides growth opportunities that motivate staff for long-term potential and retention.&nbsp; The team is important for sharing of expertise, knowledge and experience.<br>We are engaged as a team on each and every property.</p>
  <p class="gap">Every cooperative, condominium and rental building has a structure and physical plant that needs ongoing attention from ownership, management, staff and outside professionals.&nbsp; In order for building operations and projects to flow smoothly, these components must work collaboratively.&nbsp; Management is the centerpiece of this equation.&nbsp; KT7RP provides bespoke management solutions to all buildings in its portfolio.</p>
  <p>Shareholders, unit owners and tenants are all individuals who have a home that needs the appropriate level of management to ensure a quiet, safe and well-maintained environment.</p>
  <p class="point">. We manage multifamily dwellings the way they should be managed watching costs, providing quality service, creating value.<br>We create value for building resulting in increased apartment/building values.</p>
  <p class="point">. We leverage knowledge of real estate ownership, management and development to maximize appreciation and income</p>
  <p class="point">. We believe that quality management equals integrity, accountability, ownership, reliability and responsibility.</p>
  <p class="point">. We attract top-notch managers by providing ownership opportunities and income generating potential.</p>
</section>

<section class="bios">
  <h2>Daniel Reyes</h2>
  <p>Prior to co-founding KT7 Realty Partners, Daniel was the Acquisitions Manager and a Senior Property Manager at Northgate Residential New York, LLC (formerly Bleeker Lane Realty, Inc.) managing properties and locating investment opportunities for the principals of Northgate. Daniel used his management, investment and development knowledge to create and implement asset repositioning plans including renovations and re-leasing for investments in order to maximize value for investors. Daniel has managed over 1200 units in more than 30 buildings including residential and commercial owners/tenants and 50+ staff members.</p>
  <p>Daniel has experience in high end and affordable housing including rent stabilized units in the rental, coop and condo markets both from Northgate and his prior position at The Halvorsen Group in Washington, DC.&nbsp; He began working in property management upon graduation from Chesapeake State University with a degree in Economics. Daniel grew up in Minneapolis, MN.</p>
  <p>Daniel established himself as a leading manager and key investment advisor at Northgate.&nbsp; He is an entrepreneur and is parlaying his unique skills and knowledge into making KT7 one of New York City's leading property management and real estate investment firms.</p>
  <h2>Laura Brennan</h2>
  <p>Before co-founding KT7 Realty Partners, Laura was a Team Leader at Northgate Residential (formerly Bleeker Lane), managing a team of 10+ managers responsible for a portfolio of multi-family buildings varying in size, location and prominence in Manhattan, Riverdale and Queens.&nbsp; She has been in property management for 12 years.&nbsp; She also served as Vice President of Client Accounting, utilizing her accounting background and management experience to restructure the department to better serve Bleeker Lane clients.</p>
  <p>Laura has over 20 years of experience in various aspects of the management business.&nbsp; She was Board President of a large Westside Manhattan cooperative for more than 10 years.&nbsp; She began her career in New York at Meridian Financial in finance, accounting and marketing positions.&nbsp; Her passion and interest in the management business prompted her to change careers and she joined a small management company in 2002. She rose through the ranks to both lead Client Accounting and her management team.</p>
  <p>Laura is originally from San Diego, California, where she obtained her Certified Public Accounting license while working for Carrow &amp; Lindell.&nbsp; She moved to New York where she earned her Masters in Business Administration (finance) from Hudson Valley University.&nbsp; Her undergraduate degree is in accounting from Pacific Coast University.</p>
  <p>During Laura's tenure at Northgate/Bleeker Lane, she established herself as a high performing manager and leader.<br>Her broad scope of experience and education continue to be utilized by many buildings in improving financial performance, building operations and staff management.&nbsp; She is continuing to leverage these skills in building KT7RP.</p>
</section>

<svg class="crop-marks" viewBox="0 0 1200 881" aria-hidden="true">
  <g stroke="var(--crop)" stroke-width="1">
    <line x1="34" y1="0" x2="34" y2="12"/>
    <line x1="600" y1="0" x2="600" y2="12"/>
    <line x1="1164" y1="0" x2="1164" y2="12"/>
    <line x1="22" y1="22" x2="10" y2="22"/>
    <line x1="1176" y1="22" x2="1188" y2="22"/>
    <line x1="22" y1="396" x2="10" y2="396"/>
    <line x1="1176" y1="396" x2="1188" y2="396"/>
    <line x1="22" y1="454" x2="10" y2="454"/>
    <line x1="1176" y1="454" x2="1188" y2="454"/>
    <line x1="22" y1="862" x2="10" y2="862"/>
    <line x1="1176" y1="862" x2="1188" y2="862"/>
    <line x1="34" y1="870" x2="34" y2="881"/>
    <line x1="600" y1="870" x2="600" y2="881"/>
    <line x1="1164" y1="870" x2="1164" y2="881"/>
  </g>
</svg>

</body>
</html>
```